Games in Classrooms Sponsorship Brochure

We need a 4 page sponsorship booklet designed for Games in Classrooms. Games in Classrooms is a scheme that brings top GB athletes into primary schools to encourage children to lead a healthy life and raise much needed funds for schools to buy new sports equipment. We would like to see designs that are eye catching, colourful and would appeal to children. I have attached the Kids at Heart Appeal Kit (FULL PACK) for design ideas and a Word Document containing potential content (Sponsorship Form - Generic.docx) . I have also attached our brand guidelines and colour palette (Brand Guidelines PPT). WE would like to see pictures of our events and athletes to help bring the sponsorship form to life. I have attached some examples but please feel free to ask for more.

Target Market(s)

Children/Parents and Families/Friends

Requirements
Must have
• 4 pages
• Be a booklet
• Have a sponsorship form on the front
• Be eye catching
• Be colourful

```html
<!DOCTYPE html>
<html lang="en">
<head>
<meta charset="utf-8">
<title>Games in Classrooms – The Event</title>
<link rel="stylesheet" href="https://fonts.googleapis.com/css2?family=Montserrat:wght@500;600&family=Open+Sans:wght@400;700&display=swap">
<style>
  :root {
    --red: #d7263d;
    --green: #74bb38;
    --blue: #0077c0;
    --ring: #dcdcdc;
    --orange: #e85d31;
    --grass: #43a73d;
    --charcoal: #464341;
    --gold: #f4c20d;
    --ink: #333333;
    --paper: #ffffff;
    --backdrop: #e9eaeb;
  }
  html, body { margin: 0; padding: 0; width: 1200px; height: 1200px; overflow: hidden; background: var(--backdrop); }
  .page {
    position: absolute; left: 196px; top: 30px;
    width: 918px; height: 1297px;
    background: var(--paper);
    overflow: hidden;
    transform: scale(0.88); transform-origin: top left;
    font-family: "Open Sans", sans-serif; color: var(--ink);
  }
  .section-title {
    position: absolute; left: 50px; margin: 0;
    font-family: "Montserrat", sans-serif; font-weight: 600;
    font-size: 38px; letter-spacing: 0.5px; color: var(--red); line-height: 1;
  }
  .rule { position: absolute; left: 52px; height: 2px; background: var(--red); }
  .bubble {
    position: absolute; width: 344px; height: 344px; border-radius: 50%;
    box-shadow: 0 0 0 22px var(--ring);
    color: #fff; text-align: center;
    display: flex; flex-direction: column; align-items: center; justify-content: center;
    box-sizing: border-box; padding: 0 28px;
  }
  .bubble h3 { margin: 0 0 4px; font-weight: 700; font-size: 28px; line-height: 38px; }
  .bubble p { margin: 0; font-size: 18px; line-height: 25.5px; }
  .bubble--practice { left: 357px; top: -60px; background: var(--green); justify-content: flex-start; padding-top: 105px; }
  .bubble--dvd { left: 52px; top: 131px; background: var(--red); }
  .bubble--dayout { left: 580px; top: 232px; background: var(--blue); }
  .intro { position: absolute; left: 52px; margin: 0; font-size: 18px; line-height: 25px; width: 820px; }
  .exercise-figure { position: absolute; background: linear-gradient(135deg, #fbe28a, var(--gold)); opacity: 0.55; border-radius: 10px; }
  .exercise-label {
    position: absolute; width: 160px; margin-left: -80px; text-align: center;
    font-family: "Montserrat", sans-serif; font-weight: 600; font-size: 15px; color: var(--gold); top: 895px;
  }
  .goal { position: absolute; width: 230px; height: 230px; border-radius: 50%; color: #fff; }
  .goal p { position: absolute; left: 25px; top: 90px; margin: 0; font-size: 19px; line-height: 19px; }
  .goal--orange { left: 76px; top: 1089px; background: var(--orange); }
  .goal--green { left: 344px; top: 1089px; background: var(--grass); }
  .goal--dark { left: 614px; top: 1089px; background: var(--charcoal); }
  .amount {
    position: absolute; width: 120px; height: 120px; border-radius: 50%;
    background: var(--red); box-shadow: 0 0 0 7px var(--paper);
    color: #fff; font-family: "Montserrat", sans-serif; font-weight: 500; font-size: 38px;
    display: flex; align-items: center; justify-content: center;
  }
</style>
</head>
<body>
<main class="page">
  <h2 class="section-title" style="top:49px">THE EVENT</h2>
  <div class="rule" style="top:94px;width:252px"></div>

  <div class="bubble bubble--practice">
    <h3>PRACTICE</h3>
    <p>I'll practice the 4 exercises<br>before the event so I can<br>show the athlete what<br>I've learnt.</p>
  </div>
  <div class="bubble bubble--dvd">
    <h3>THE DVD<br>ASSEMBLY</h3>
    <p>I'll watch a DVD in assembly<br>to reveal which GB athlete is<br>visiting my school and what sport<br>they compete in.<br>I'll also learn the exercises that<br>I'll be doing with the athlete<br>on the day</p>
  </div>
  <div class="bubble bubble--dayout">
    <h3>THE<br>EVENT DAY</h3>
    <p>I'll complete the fitness<br>circuit alongside the athlete,<br>listen to an inspirational<br>assembly and ask any<br>questions I may have.</p>
  </div>

  <h2 class="section-title" style="top:598px">THE EXERCISES</h2>
  <div class="rule" style="top:643px;width:813px"></div>
  <p class="intro" style="top:658px">I will complete as many of the following exercises as I can in 1 minute intervals</p>

  <div class="exercise-figure" role="img" aria-label="Outline figure doing leg drives" style="left:99px;top:784px;width:195px;height:90px"></div>
  <div class="exercise-figure" role="img" aria-label="Outline figure doing star jumps" style="left:292px;top:696px;width:162px;height:180px"></div>
  <div class="exercise-figure" role="img" aria-label="Outline figure doing spotty dogs" style="left:479px;top:696px;width:115px;height:173px"></div>
  <div class="exercise-figure" role="img" aria-label="Outline figure doing push ups" style="left:624px;top:764px;width:173px;height:110px"></div>
  <span class="exercise-label" style="left:196px">Leg Drives</span>
  <span class="exercise-label" style="left:373px">Star Jumps</span>
  <span class="exercise-label" style="left:536px">Spotty Dogs</span>
  <span class="exercise-label" style="left:711px">Push Ups</span>

  <h2 class="section-title" style="top:951px">AFTER THE EVENT</h2>
  <div class="rule" style="top:996px;width:813px"></div>
  <p class="intro" style="top:1011px">I'll have one week to collect up my sponsorship money and then I will need to return the front two pages of this form to the school office.</p>

  <div class="goal goal--orange"><p>Could buy<br>my school<br>15 footballs</p></div>
  <div class="amount" style="left:205px;top:1089px">£100</div>
  <div class="goal goal--green"><p>Could buy<br>my school<br>2 basketball<br>hoops</p></div>
  <div class="amount" style="left:475px;top:1089px">£250</div>
  <div class="goal goal--dark"><p>Could buy<br>my school<br>a gym mat trolley<br>&amp; 5 gym mats</p></div>
  <div class="amount" style="left:745px;top:1089px">£500</div>
</main>
</body>
</html>
```